Operator Qualification Testing Flyer

I have a 8x10 basic flyer that I created usin InDesign for one of our services our company provides. I would like to see more options for the layout and general design of the flyer. This flyer will be used as a template for the other services we provide. I will include the InDesign Folder with all the logos and images. Please feel free to use any logo design within the folder and you can change the font and/or colors as needed. I would like the final output in a Indesign package folder to be used in InDesign 2021

Target Market(s)

Business to Business marketing in the Oil and Gas industry

Font styles to use
Sans Serif

Colors
85cae6
85acd3
3377b5
0355a3
0792cd
ffffff
cedeed

Requirements
Must have
• I included/attached a couple of brochures styles that I do like.

```html
<!DOCTYPE html>
<html lang="en">
<head>
<meta charset="UTF-8">
<title>Pipeline OQ Testing Flyer</title>
<link rel="stylesheet" href="https://fonts.googleapis.com/css2?family=Archivo:wght@700;800&family=Open+Sans:wght@400;600&display=swap">
<style>
  :root {
    --sky: #85cae6;
    --steel: #85acd3;
    --blue: #3377b5;
    --navy: #0355a3;
    --cyan: #0792cd;
    --white: #ffffff;
    --mist: #cedeed;
    --teal-dark: #1f5d70;
    --ink: #222629;
    --text: #2b2b2b;
    --footer: #c9eef8;
    --page-bg: #e6e8ea;
  }
  * { box-sizing: border-box; margin: 0; padding: 0; }
  html, body { width: 900px; height: 1200px; overflow: hidden; }
  body { background: var(--page-bg); position: relative; font-family: "Open Sans", sans-serif; }

  .flyer {
    position: absolute; left: 30px; top: 75px;
    width: 722px; height: 902px;
    background: var(--white);
    transform: scale(1.1634); transform-origin: top left;
    overflow: hidden;
  }
  .hero { position: absolute; left: 0; top: 0; width: 722px; height: 620px; }

  .brand { position: absolute; left: 45px; top: 88px; display: flex; align-items: center; gap: 10px; }
  .brand-dot { width: 34px; height: 34px; border-radius: 50%; background: var(--cyan); }
  .brand-name { font-family: "Archivo", sans-serif; font-weight: 700; font-size: 20px; line-height: 1.1; color: var(--teal-dark); }

  .title { position: absolute; left: 150px; top: 232px; width: 430px; text-align: right;
    font-family: "Archivo", sans-serif; font-weight: 800; color: var(--white);
    -webkit-text-stroke: 1.5px var(--ink); text-shadow: 2px 2px 4px rgba(0,0,0,.35); line-height: 1; }
  .title .line1 { display: block; font-size: 58px; letter-spacing: 1px; }
  .title .line2 { display: block; font-size: 54px; letter-spacing: 3px; margin-top: 6px; }

  .pill { position: absolute; left: 458px; top: 537px; width: 215px; height: 27px; border-radius: 14px;
    background: var(--teal-dark); color: var(--white); font-family: "Archivo", sans-serif; font-weight: 700;
    font-size: 18px; text-align: center; line-height: 27px; letter-spacing: .5px; }

  .icon-circle { position: absolute; width: 54px; height: 54px; border-radius: 50%; background: var(--ink); }
  .icon-circle.teal { background: var(--teal-dark); }
  .icon-circle.small { width: 32px; height: 32px; }

  .section-heading { position: absolute; left: 100px; font-size: 19px; color: var(--teal-dark); font-weight: 400; white-space: nowrap; }
  .section-heading strong { color: var(--ink); font-weight: 400; }
  .section-body { position: absolute; left: 47px; width: 330px; font-size: 10.2px; line-height: 1.32; color: var(--text); text-align: justify; }

  .provide-item { position: absolute; left: 423px; width: 266px; padding-left: 10px; border-left: 2px solid var(--ink);
    font-size: 10.2px; line-height: 1.32; color: var(--text); text-align: justify; }

  .contact { position: absolute; left: 448px; font-size: 10px; color: var(--ink); display: flex; align-items: center; gap: 8px; }
  .contact .phone { font-size: 17px; font-weight: 600; color: var(--teal-dark); }
  .contact .email { font-size: 11px; letter-spacing: 2.6px; }

  .footer-band { position: absolute; left: 0; top: 868px; width: 722px; height: 25px; background: var(--footer);
    text-align: center; font-size: 10.5px; letter-spacing: 3px; line-height: 25px; color: var(--ink); }
</style>
</head>
<body>
  <div class="flyer">
    <svg class="hero" viewBox="0 0 722 620" xmlns="http://www.w3.org/2000/svg">
      <defs>
        <linearGradient id="soil" x1="0" y1="0" x2="1" y2="1">
          <stop offset="0" stop-color="#a38b6c"/>
          <stop offset=".5" stop-color="#8a7258"/>
          <stop offset="1" stop-color="#6f5a45"/>
        </linearGradient>
        <linearGradient id="haze" x1="0" y1="0" x2="1" y2="0">
          <stop offset="0" stop-color="#e8eef2"/>
          <stop offset="1" stop-color="#cfdbe3"/>
        </linearGradient>
      </defs>
      <polygon points="0,590 722,370 722,620 0,620" fill="url(#haze)" opacity=".7"/>
      <g role="img" aria-label="Photo of a yellow pipelayer tractor working on a dirt pipeline right-of-way">
        <polygon points="0,230 722,5 722,370 0,590" fill="url(#soil)"/>
      </g>
      <polygon points="0,592 722,372 722,384 0,604" fill="var(--sky)"/>
      <polygon points="330,491 430,460 430,472 330,503" fill="#2c3136"/>
      <polygon points="0,604 180,549 180,562 0,617" fill="var(--blue)"/>
      <g role="img" aria-label="Round yellow petroleum pipeline warning marker sign">
        <circle cx="550" cy="440" r="73" fill="#f2c318" stroke="#1e1e1e" stroke-width="4"/>
      </g>
    </svg>

    <div class="brand">
      <span class="brand-dot"></span>
      <span class="brand-name">Ridgeway Controls<br>Inc.</span>
    </div>

    <h1 class="title"><span class="line1">PIPELINE OQ</span><span class="line2">TESTING</span></h1>

    <div class="pill">WHAT WE PROVIDE</div>

    <div class="icon-circle" style="left:36px; top:579px;"></div>
    <h2 class="section-heading" style="top:593px;">What Is Operator <strong>Qualification?</strong></h2>
    <p class="section-body" style="top:633px;">Operator Qualifications (OQ) for DOT Oil/Gas Pipelines are requirements set by Department of Transportation (DOT) and Pipeline and Hazardous Materials Safety Administration (PHMSA). To assure safety in the transport of hazardous gases and liquids in the nation's pipelines, pipeline operators who perform covered tasks must be qualified. Qualified means that an individual has been evaluated and can perform assigned covered tasks and recognize and react to abnormal operating conditions</p>

    <div class="icon-circle teal" style="left:36px; top:747px;"></div>
    <h2 class="section-heading" style="top:763px;">What Are <strong>Covered Tasks?</strong></h2>
    <p class="section-body" style="top:800px;">Covered tasks are defined in an operator's written plan which defines specific job functions or activities personnel are qualified to perform on a pipeline facility.</p>

    <p class="provide-item" style="top:579px;">Ridgeway Controls Inc. utilizes NPTB pipeline program to administer OQ assessment testing on 127 covered tasks</p>
    <p class="provide-item" style="top:633px;">Upon completion of OQ testing the information is first transferred to NPTB's Registry System and automatically uploaded to VendorNet.</p>
    <p class="provide-item" style="top:687px;">In addition to the benefits provided by VendorNet's database, the NPTB Registry System houses all the completion information allowing candidates to share their training information and employers to verify successful covered task and level completions</p>

    <div class="icon-circle small" style="left:409px; top:776px;"></div>
    <div class="contact" style="top:781px;">call for more information <span class="phone">555-014-2876</span></div>
    <div class="icon-circle small teal" style="left:409px; top:815px;"></div>
    <div class="contact" style="top:822px;"><span class="email">info@ridgeway-controls.co</span></div>

    <div class="footer-band">www.yourwebsite.com</div>
  </div>
</body>
</html>
```